Business Card Design Project

I own a dental practice and would like to use a logo that was recently designed to make business cards.
I am looking for a clean card with the following information on the card.

Halvorsen Dental Center (Using the logo)
Martin L. Halvorsen, D.D.S.
7234 Pinewick Ave. Suite B
Colorado Springs, CO 80547
(719) 482-6130
halvorsendentalcenter@mailbox-example.net
www.halvorsendentalcenter.example

Also a list of items on the back:
Services include

Family Dentistry
Cosmetic
Whitening
Tooth Colored Fillings
Crowns/Bridges
Implants/Tooth Replacement
Dentures
Root Canals
Updates

Just an FYI, I added an email address and website address.

I also added my Pic.  Please give designs with and without the pic

Thanks

Target Market(s)

20-70 U.S. Female that handles the household budget.

Industry/Entity Type

Dental

Requirements
Must have
• The logo is key. The color scheme of the logo is also key. The back of the business card should have the list of Dental Services offered at the practice. The front should be clean and professional looking. No cartoons. I will also include a picture of myself. I think that the final card may or may not include this picture, so the card designs should come with and without the picture. USE THE BLUE LOGO ONLY!!!
Should not have
• NO teeth should be on the card.

```html
<!DOCTYPE html>
<html lang="en">
<head>
<meta charset="utf-8">
<title>Halvorsen Dental Center – Business Card</title>
<link href="https://fonts.googleapis.com/css2?family=Lato:wght@400;700&display=swap" rel="stylesheet">
<style>
  :root {
    --page-bg: #eef1f3;
    --card-center: #3283a4;
    --card-edge: #1d5a75;
    --ink: #ffffff;
    --ink-soft: rgba(255,255,255,0.85);
    --leaf: rgba(255,255,255,0.22);
    --shadow: rgba(20,40,55,0.35);
  }
  * { box-sizing: border-box; margin: 0; padding: 0; }
  html, body { width: 1200px; height: 1000px; overflow: hidden; }
  body {
    background: var(--page-bg);
    font-family: "Lato", Arial, sans-serif;
    color: var(--ink);
    position: relative;
  }
  .card {
    position: absolute;
    top: 345px;
    width: 555px;
    height: 310px;
    border-radius: 12px;
    background: radial-gradient(ellipse at 55% 40%, var(--card-center) 0%, var(--card-edge) 100%);
    box-shadow: 0 6px 18px var(--shadow);
    overflow: hidden;
  }
  .card-front { left: 30px; }
  .card-back { left: 615px; }

  /* front */
  .brand {
    position: absolute;
    top: 46px; left: 0; width: 100%;
    text-align: center;
  }
  .brand-name {
    display: inline-flex; align-items: center; gap: 9px;
    font-size: 21px; font-weight: 700; letter-spacing: 0.3px;
  }
  .brand-dot { width: 12px; height: 12px; border-radius: 50%; background: var(--ink); }
  .brand-tagline {
    margin-top: 6px;
    font-size: 9.5px; letter-spacing: 1.6px; color: var(--ink-soft);
  }
  .divider { position: absolute; top: 140px; left: 0; }
  .dentist {
    position: absolute; top: 200px; left: 36px;
    text-align: center; font-size: 21px; line-height: 1.7;
  }
  .contact-list {
    position: absolute; top: 180px; left: 268px;
    list-style: none; font-size: 11.5px; line-height: 1.2;
  }
  .contact-list li { display: flex; align-items: flex-start; gap: 6px; margin-bottom: 7px; }
  .contact-icon { width: 16px; height: 16px; flex: none; }

  /* back */
  .tree-art {
    position: absolute; left: 190px; top: 34px;
    width: 170px; height: 262px;
    border-radius: 50% 50% 8px 8px / 40% 40% 8px 8px;
    background: radial-gradient(ellipse at 50% 35%, var(--leaf) 0%, rgba(255,255,255,0.06) 75%, transparent 100%);
  }
  .service {
    position: absolute; font-size: 14.5px; white-space: nowrap;
  }
  .service-right { text-align: right; }
</style>
</head>
<body>

<section class="card card-front" aria-label="Business card front">
  <div class="brand">
    <div class="brand-name"><span class="brand-dot"></span>Halvorsen Dental Center</div>
    <div class="brand-tagline">FAMILY · COSMETIC · IMPLANTS</div>
  </div>

  <svg class="divider" width="555" height="26" viewBox="0 0 555 26">
    <polyline points="0,10 100,10 120,26 140,10 555,10" fill="none" stroke="#ffffff" stroke-width="2"/>
  </svg>

  <div class="dentist">Martin L. Halvorsen<br>D.D.S</div>

  <ul class="contact-list">
    <li>
      <svg class="contact-icon" viewBox="0 0 16 16"><circle cx="8" cy="8" r="8" fill="#fff"/><path d="M5 4.5l1.5-.5 1 2-1 .8c.4 1 1.1 1.7 2 2.1l.8-1 2 1-.4 1.5c-3 .3-6.2-2.9-5.9-5.9z" fill="#245f7a"/></svg>
      <span>(719) 482-6130</span>
    </li>
    <li>
      <svg class="contact-icon" viewBox="0 0 16 16"><circle cx="8" cy="8" r="8" fill="#fff"/><rect x="4" y="5" width="8" height="6" fill="none" stroke="#245f7a" stroke-width="1.2"/><polyline points="4,5 8,8.5 12,5" fill="none" stroke="#245f7a" stroke-width="1.2"/></svg>
      <span>halvorsendentalcenter@mailbox-example.net</span>
    </li>
    <li>
      <svg class="contact-icon" viewBox="0 0 16 16"><circle cx="8" cy="8" r="8" fill="#fff"/><circle cx="8" cy="8" r="4.5" fill="none" stroke="#245f7a" stroke-width="1"/><ellipse cx="8" cy="8" rx="2" ry="4.5" fill="none" stroke="#245f7a" stroke-width="1"/><line x1="3.5" y1="8" x2="12.5" y2="8" stroke="#245f7a" stroke-width="1"/></svg>
      <span>www.halvorsendentalcenter.example</span>
    </li>
    <li>
      <svg class="contact-icon" viewBox="0 0 16 16"><circle cx="8" cy="8" r="8" fill="#fff"/><path d="M8 3.5a3 3 0 0 1 3 3c0 2.2-3 5.8-3 5.8s-3-3.6-3-5.8a3 3 0 0 1 3-3z" fill="#245f7a"/><circle cx="8" cy="6.5" r="1" fill="#fff"/></svg>
      <span>7234 Pinewick Ave. Suite B<br>Colorado Springs, CO 80547</span>
    </li>
  </ul>
</section>

<section class="card card-back" aria-label="Business card back">
  <div class="tree-art" role="img" aria-label="Tree illustration with scattered leaves"></div>

  <div class="service" style="left:262px; top:38px;">• Implants/Tooth Replacement</div>
  <div class="service service-right" style="right:358px; top:59px;">Whitening •</div>
  <div class="service service-right" style="right:374px; top:99px;">Crowns/Bridges •</div>
  <div class="service" style="left:348px; top:91px;">• Family Dentistry</div>
  <div class="service" style="left:370px; top:133px;">• Cosmetic</div>
  <div class="service service-right" style="right:398px; top:158px;">Dentures •</div>
  <div class="service service-right" style="right:360px; top:203px;">Root Canals •</div>
  <div class="service" style="left:312px; top:227px;">• Tooth Colored Fillings</div>
</section>

</body>
</html>
```